letterhead design for a investing company*

Design an appealing business letterhead to match with our existing logo and attract new customers. Our customers are mainly corporate managers which are detail oriented and judge the company ability to perform a good service based on small details. A professional letterhead will give a good first impression.

Target Market(s)

New customers and business owners

Industry/Entity Type

Marketplace

Font styles to use
Sans Serif
Script

Requirements
Must have
• Must be a professional and elegant design that attracts interest from people who receives it

```html
<!DOCTYPE html>
<html lang="en">
<head>
<meta charset="UTF-8">
<title>Northvale Letterhead</title>
<link rel="stylesheet" href="https://fonts.googleapis.com/css2?family=Lato:wght@400;900&family=Roboto+Condensed:wght@300&family=Great+Vibes&display=swap">
<style>
  :root {
    --backdrop: #d6d6d6;
    --paper: #ffffff;
    --navy: #14213d;
    --gold: #f7b718;
    --body-text: #4f4f4f;
  }
  * { margin: 0; padding: 0; box-sizing: border-box; }
  html, body {
    width: 1056px;
    height: 1200px;
    overflow: hidden;
    background: var(--backdrop);
  }
  .letterhead {
    position: absolute;
    left: 104px;
    top: 0;
    width: 848px;
    height: 1200px;
    background: var(--paper);
  }
  .brand {
    position: absolute;
    left: 53px;
    top: 96px;
    display: flex;
    align-items: center;
    gap: 12px;
  }
  .brand-dot {
    width: 38px;
    height: 38px;
    border-radius: 50%;
    background: var(--gold);
  }
  .brand-name {
    font-family: "Lato", sans-serif;
    font-weight: 900;
    font-size: 44px;
    line-height: 1;
    color: var(--navy);
    letter-spacing: -0.5px;
  }
  .contact {
    position: absolute;
    right: 52px;
    top: 82px;
    font-family: "Lato", sans-serif;
    font-size: 14px;
    color: var(--navy);
    text-align: right;
  }
  .contact-address { line-height: 18px; margin-right: 5px; margin-bottom: 8px; }
  .contact-line {
    display: flex;
    justify-content: flex-end;
    align-items: center;
    gap: 12px;
    height: 20.5px;
  }
  .contact-icon { width: 14px; height: 14px; flex: none; }
  .header-rule {
    position: absolute;
    left: 52px;
    right: 52px;
    top: 204px;
    height: 1px;
    background: var(--gold);
  }
  .letter-body {
    position: absolute;
    left: 82px;
    width: 688px;
    top: 366px;
    font-family: "Roboto Condensed", sans-serif;
    font-weight: 300;
    font-size: 17.5px;
    line-height: 29.5px;
    color: var(--body-text);
  }
  .letter-body p { text-align: justify; margin-bottom: 29.5px; }
  .letter-body .salutation { margin-bottom: 14.5px; }
  .closing {
    position: absolute;
    left: 82px;
    top: 967px;
    font-family: "Roboto Condensed", sans-serif;
    font-weight: 300;
    font-size: 17.5px;
    color: var(--body-text);
  }
  .signature {
    position: absolute;
    left: 78px;
    top: 1002px;
    font-family: "Great Vibes", cursive;
    font-size: 36px;
    color: var(--gold);
  }
  .footer-band {
    position: absolute;
    left: 0;
    right: 0;
    bottom: 0;
    height: 14px;
    background: var(--gold);
  }
</style>
</head>
<body>
  <main class="letterhead">
    <div class="brand">
      <span class="brand-dot"></span>
      <span class="brand-name">Northvale</span>
    </div>

    <div class="contact">
      <div class="contact-address">1234 First Line Address<br>5678 Second Line Address</div>
      <div class="contact-line">
        <span>1234567890</span>
        <svg class="contact-icon" viewBox="0 0 24 24" fill="none" stroke="var(--gold)" stroke-width="2.2" stroke-linecap="round" stroke-linejoin="round"><path d="M22 16.9v3a2 2 0 0 1-2.2 2 19.8 19.8 0 0 1-8.6-3.1 19.5 19.5 0 0 1-6-6A19.8 19.8 0 0 1 2.1 4.2 2 2 0 0 1 4.1 2h3a2 2 0 0 1 2 1.7c.1 1 .4 1.9.7 2.8a2 2 0 0 1-.5 2.1L8 9.9a16 16 0 0 0 6 6l1.3-1.3a2 2 0 0 1 2.1-.4c.9.3 1.8.6 2.8.7a2 2 0 0 1 1.8 2z"/><path d="M15 2a7 7 0 0 1 7 7M15 6a3 3 0 0 1 3 3"/></svg>
      </div>
      <div class="contact-line">
        <span>info@yourmail.com</span>
        <svg class="contact-icon" viewBox="0 0 24 24"><rect x="1" y="4" width="22" height="16" fill="var(--gold)"/><path d="M1 4l11 9 11-9M1 20l8-8M23 20l-8-8" fill="none" stroke="#fff" stroke-width="1.6"/></svg>
      </div>
      <div class="contact-line">
        <span>www.yourwebsite.com</span>
        <svg class="contact-icon" viewBox="0 0 24 24" fill="none" stroke="var(--gold)" stroke-width="1.8"><circle cx="12" cy="12" r="10"/><ellipse cx="12" cy="12" rx="4.5" ry="10"/><path d="M2 12h20M4 6.5h16M4 17.5h16"/></svg>
      </div>
    </div>

    <div class="header-rule"></div>

    <section class="letter-body">
      <p class="salutation">Dear Sir/Mam,</p>
      <p>Contrary to popular belief, Lorem Ipsum is not simply random text. It has roots in a piece of classical Latin literature from 45 BC, making it over 2000 years old. Edwin Harcourt, a Latin professor at Alder Ridge College in Virginia, looked up one of the more obscure Latin words, consectetur.</p>
      <p>Lorem Ipsum comes from sections 1.10.32 and 1.10.33 of "de Finibus Bonorum et Malorum" (The Extremes of Good and Evil) by Aurelian, written in 45 BC. This book is a treatise on the theory of ethics, very popular during the Renaissance. The first line of Lorem Ipsum.</p>
      <p>The standard chunk of Lorem Ipsum used since the 1500s is reproduced below for those interested. Sections 1.10.32 and 1.10.33 from "de Finibus Bonorum et Malorum" by Aurelian are also reproduced in their exact original.</p>
      <p>The standard chunk of Lorem Ipsum used since the 1500s is reproduced below for those interested.</p>
    </section>

    <div class="closing">Best Regards</div>
    <div class="signature">Harlow</div>

    <div class="footer-band"></div>
  </main>
</body>
</html>
```